Project Title:
Dental Implant Overdenture Flyer (Retirement Village Target)
Objective:
Create a clean, trustworthy, and reassuring flyer aimed at older adults (60–85 years old) who struggle with loose dentures. The goal is to educate them about implant-retained “clip-on” dentures and encourage them to book a consultation.
Tone & Feel:
Warm, caring, non-intimidating
Premium but not “salesy”
Medical but easy to understand
Focus on improving quality of life (confidence, eating, comfort)
Target Audience:
Retirees / pensioners
Existing denture wearers
People frustrated with loose or uncomfortable dentures
Key Message:
“You don’t have to live with loose dentures anymore.”
Design Style:
Clean, minimal, modern
Soft colours (blues, greens, warm neutrals)
Easy-to-read large font
High contrast for older eyes
Avoid clutter
Imagery Suggestions:
Smiling older adults (natural, not stocky/overly staged)
Before/after lifestyle (eating, laughing, socialising)
Simple diagram showing denture clipping onto implants
Avoid graphic surgical images
Layout Suggestions:
A5 or DL flyer
Clear sections with headings
Icons for benefits
Strong call-to-action at bottom
HEADLINE (big and bold)
Tired of Loose Dentures?
Discover Secure “Clip-On” Teeth
🔹 PROBLEM SECTION
Do your dentures:
Slip or move when eating?
Make it hard to chew certain foods?
Feel uncomfortable or loose?
Affect your confidence when speaking or smiling?
You’re not alone — and there is a better solution.
🔹 SOLUTION SECTION
Implant-Retained “Clip-On” Dentures
We can secure your denture using just 2 dental implants, allowing your teeth to:
✔ Stay firmly in place
✔ Improve your ability to eat
✔ Feel more comfortable
✔ Boost your confidence
🔹 SIMPLE EXPLANATION (very important)
Small titanium implants are gently placed in the jaw.
Your denture then clips securely onto them, stopping movement.
🔹 PRICE SECTION (highlight this clearly)
$12,000
Includes:
2 dental implants
A brand new custom overdenture
Does not include sedation or extractions (if needed)
🔹 SEDATION
Sedation is available for comfort.
If you hold a pensioner card, you may receive a significant Vantrel rebate, often resulting in minimal out-of-pocket costs for sedation.
🔹 TRUST / REASSURANCE
Experienced implant clinician
Gentle, patient-focused care
Modern technology and techniques
🔹 CALL TO ACTION (VERY IMPORTANT)
Book a Free Consultation
📞 Call: 08 5127 3046
🌐 Visit: www.brolvenclinic.com.au
📍 Located near Tallowmere shopping centre
🔹 OPTIONAL TAGLINE
Eat Better. Feel Better. Smile with Confidence Again.
Please include some photos to illustrate what a clip on denture looks like with two implants.

```html
<!DOCTYPE html>
<html lang="en">
<head>
<meta charset="utf-8">
<title>Brolven Dental Clinic – Clip-On Denture Flyer</title>
<link rel="stylesheet" href="https://fonts.googleapis.com/css2?family=Montserrat:wght@400;500;600;700;800&display=swap">
<style>
  :root {
    --page-bg: #ececec;
    --paper: #ffffff;
    --teal-deep: #1d8fa7;
    --teal-box: #1c93ad;
    --teal-soft: #4dc0bb;
    --teal-line: #2aa6b3;
    --ink: #1d1d1d;
    --ink-soft: #2b2b2b;
    --ink-muted: #555555;
    --photo-light: #eef5fa;
    --photo-mid: #bcd8ea;
  }
  * { box-sizing: border-box; margin: 0; padding: 0; }
  html, body { width: 1200px; height: 1200px; overflow: hidden; }
  body {
    background: var(--page-bg);
    font-family: "Montserrat", sans-serif;
    color: var(--ink);
    position: relative;
  }
  .flyer {
    position: absolute;
    top: 65px;
    width: 506px;
    height: 1070px;
    background: var(--paper);
    overflow: hidden;
    text-align: center;
  }
  .flyer--front { left: 71px; }
  .flyer--back { left: 624px; }
  .abs { position: absolute; left: 0; right: 0; }

  .brand {
    top: 120px;
    display: flex;
    align-items: center;
    justify-content: center;
    gap: 14px;
  }
  .brand__mark {
    width: 30px; height: 30px;
    border-radius: 50%;
    background: var(--teal-deep);
  }
  .brand__name {
    font-weight: 600;
    font-size: 27px;
    letter-spacing: 0.04em;
    color: var(--teal-deep);
  }

  /* Front */
  .headline {
    top: 298px;
    font-weight: 800;
    font-size: 45px;
    line-height: 44px;
    color: var(--teal-deep);
    letter-spacing: 0.005em;
  }
  .subhead-band {
    top: 389px;
    height: 32px;
    background: var(--teal-soft);
    color: #fff;
    font-weight: 700;
    font-size: 21px;
    line-height: 32px;
  }
  .problem__title {
    top: 452px;
    font-weight: 700;
    font-size: 20px;
  }
  .problem__list {
    top: 496px;
    list-style: none;
    font-size: 17px;
    line-height: 22px;
    color: var(--ink-soft);
  }
  .solution-box {
    top: 606px;
    left: 20px; right: 20px;
    height: 88px;
    background: var(--teal-box);
    color: #fff;
    font-size: 17px;
    line-height: 22px;
    display: flex;
    flex-direction: column;
    justify-content: center;
  }
  .solution__intro {
    top: 752px;
    font-size: 17px;
    line-height: 22px;
    color: var(--ink-soft);
  }
  .benefits {
    top: 818px;
    left: 71px; right: auto;
    list-style: none;
    text-align: left;
    font-size: 17px;
    line-height: 22px;
    color: var(--ink-soft);
  }
  .benefits li { display: flex; align-items: center; gap: 7px; }
  .benefits svg { width: 11px; height: 11px; flex: none; }
  .front-wave { bottom: 0; height: 280px; }
  .front-wave svg { display: block; width: 100%; height: 100%; }
  .tagline {
    bottom: 16px;
    font-weight: 700;
    font-size: 14px;
    line-height: 18px;
    color: #fff;
  }

  /* Back */
  .explain {
    top: 262px;
    font-size: 17px;
    line-height: 22px;
    color: var(--ink-soft);
  }
  .price {
    top: 372px;
    font-weight: 800;
    font-size: 58px;
    line-height: 60px;
    color: var(--teal-deep);
  }
  .price__includes {
    top: 434px;
    font-size: 17px;
    line-height: 21px;
    color: var(--ink-soft);
  }
  .price__excludes {
    top: 480px;
    font-size: 13px;
    line-height: 18px;
    font-style: normal;
    color: var(--ink-muted);
  }
  .sedation {
    top: 518px;
    font-size: 17px;
    line-height: 22px;
    color: var(--ink-soft);
  }
  .sedation__rebate {
    top: 544px;
    left: 40px; right: 40px;
    font-size: 13px;
    line-height: 18px;
    color: var(--ink-muted);
  }
  .photo-band {
    top: 619px;
    height: 154px;
    background: linear-gradient(100deg, var(--photo-light) 0%, var(--photo-mid) 45%, #d7e8f3 70%, #9fc4dc 100%);
  }
  .trust {
    top: 795px;
    list-style: none;
    font-size: 17px;
    line-height: 22px;
    color: var(--ink-soft);
  }
  .cta {
    bottom: 0;
    height: 182px;
    background: var(--teal-soft);
    color: #fff;
  }
  .cta__title {
    margin-top: 36px;
    font-weight: 700;
    font-size: 18px;
  }
  .cta__details {
    margin-top: 22px;
    list-style: none;
    font-size: 17px;
    line-height: 22px;
  }
</style>
</head>
<body>

  <section class="flyer flyer--front">
    <div class="abs brand">
      <span class="brand__mark"></span>
      <span class="brand__name">Brolven Dental Clinic</span>
    </div>

    <h1 class="abs headline">TIRED OF LOOSE<br>DENTURES?</h1>
    <p class="abs subhead-band">Discover Secure “Clip-On” Teeth</p>

    <h2 class="abs problem__title">Do your dentures:</h2>
    <ul class="abs problem__list">
      <li>Slip or move when eating?</li>
      <li>Make it hard to chew certain foods?</li>
      <li>Feel uncomfortable or loose?</li>
      <li>Affect your confidence when speaking or smiling?</li>
    </ul>

    <div class="abs solution-box">
      <p>You’re not alone — and there is a better solution.</p>
      <p>Implant-Retained “Clip-On” Dentures</p>
    </div>

    <div class="abs front-wave" aria-hidden="true">
      <svg viewBox="0 0 506 280" preserveAspectRatio="none">
        <rect width="506" height="280" fill="var(--teal-soft)"/>
        <path d="M0 0 H506 V70 C490 160 420 210 300 215 C200 218 90 200 0 150 Z" fill="var(--paper)"/>
        <path d="M0 140 C70 190 180 228 300 226 C400 224 470 200 506 170" fill="none" stroke="var(--teal-line)" stroke-width="3"/>
      </svg>
    </div>

    <p class="abs solution__intro">We can secure your denture using just 2<br>dental implants, allowing your teeth to:</p>
    <ul class="abs benefits">
      <li><svg viewBox="0 0 12 12"><path d="M1.5 6.5 L4.5 9.5 L10.5 2.5" fill="none" stroke="var(--ink)" stroke-width="2"/></svg>Stay firmly in place</li>
      <li><svg viewBox="0 0 12 12"><path d="M1.5 6.5 L4.5 9.5 L10.5 2.5" fill="none" stroke="var(--ink)" stroke-width="2"/></svg>Improve your ability to eat</li>
      <li><svg viewBox="0 0 12 12"><path d="M1.5 6.5 L4.5 9.5 L10.5 2.5" fill="none" stroke="var(--ink)" stroke-width="2"/></svg>Feel more comfortable</li>
      <li><svg viewBox="0 0 12 12"><path d="M1.5 6.5 L4.5 9.5 L10.5 2.5" fill="none" stroke="var(--ink)" stroke-width="2"/></svg>Boost your confidence</li>
    </ul>

    <p class="abs tagline">Eat Better. Feel Better. Smile with Confidence Again.</p>
  </section>

  <section class="flyer flyer--back">
    <div class="abs brand">
      <span class="brand__mark"></span>
      <span class="brand__name">Brolven Dental Clinic</span>
    </div>

    <p class="abs explain">Small titanium implants are gently<br>placed in the jaw.<br>Your denture then clips securely onto<br>them, stopping movement.</p>

    <p class="abs price">$12,000</p>
    <p class="abs price__includes">2 dental implants<br>A brand new custom overdenture</p>
    <p class="abs price__excludes">Does not include sedation or extractions (if needed)</p>

    <p class="abs sedation">Sedation is available for comfort.</p>
    <p class="abs sedation__rebate">If you hold a pensioner card, you may receive a significant Vantrel rebate, often resulting in minimal out-of-pocket costs for sedation.</p>

    <div class="abs photo-band" role="img" aria-label="Photo of a clip-on overdenture fitted onto two dental implants in the lower jaw"></div>

    <ul class="abs trust">
      <li>Experienced implant clinician</li>
      <li>Gentle, patient-focused care</li>
      <li>Modern technology and techniques</li>
    </ul>

    <div class="abs cta">
      <p class="cta__title">Book a Free Consultation</p>
      <ul class="cta__details">
        <li>08 5127 3046</li>
        <li>www.brolvenclinic.com.au</li>
        <li>Located near Tallowmere shopping centre</li>
      </ul>
    </div>
  </section>

</body>
</html>
```